Tolven Payment Processing & money transfer Application

I would like a design of an all in one payment processing and money transfer application used to send money, receive money, pay or purchase products and services. It should have account information which must include telephone information.

Target Market(s)

Consumer, small and medium size businesses - FinTech

Industry/Entity Type

E-Commerce

Font styles to use
Sans Serif

Colors
c5dd76
faa54b
ffcf3e
f04a50

Requirements
Must have
• Send Money
• Receive Money
• Request Money
• Make Payment - card processing
• Accept Payment - card processing
• Pay bills
Nice to have
• QR code or pin per transaction
• Transaction history
Should not have
• Personalization

```html
<!DOCTYPE html>
<html lang="en">
<head>
<meta charset="utf-8">
<title>Tolven – Support</title>
<link rel="stylesheet" href="https://fonts.googleapis.com/css2?family=Roboto:wght@400;500&display=swap">
<style>
  :root {
    --brand-red: #f04a50;
    --backdrop: #ece6ee;
    --surface: #ffffff;
    --search-bg: #f7f7f7;
    --section-bg: #f0f0f0;
    --divider: #e6e6e6;
    --text-main: #3a3a3a;
    --text-heading: #222222;
    --text-muted: #8a8a8a;
    --icon: #555555;
    --online: #2ee82e;
  }
  * { box-sizing: border-box; margin: 0; padding: 0; }
  html, body {
    width: 1200px; height: 1200px; overflow: hidden;
    background: var(--backdrop);
    font-family: "Roboto", Arial, sans-serif;
  }
  .screen {
    position: absolute; left: 340px; top: 35px;
    width: 520px; height: 1131px;
    background: var(--surface);
    border-radius: 44px;
    overflow: hidden;
    display: flex; flex-direction: column;
    box-shadow: 0 20px 50px rgba(60, 20, 50, .18);
  }
  .app-header {
    height: 163px; background: var(--brand-red); color: #fff;
    position: relative; flex: none;
  }
  .status-bar {
    position: absolute; top: 18px; left: 44px; right: 22px;
    display: flex; justify-content: space-between; align-items: center;
  }
  .status-time { font-size: 20px; font-weight: 500; }
  .status-icons { display: flex; gap: 6px; align-items: center; }
  .title-bar {
    position: absolute; top: 106px; left: 29px; right: 29px;
    display: flex; justify-content: space-between; align-items: center;
  }
  .title-bar h1 { font-size: 26px; font-weight: 400; }
  .search {
    height: 50px; flex: none; background: var(--search-bg);
    display: flex; align-items: center; padding-left: 28px; gap: 20px;
    color: var(--text-muted); font-size: 17px;
  }
  .section-label {
    height: 47px; flex: none; background: var(--section-bg);
    display: flex; align-items: center; padding-left: 29px;
    font-size: 18px; color: var(--text-heading);
  }
  .topic {
    flex: none; display: flex; align-items: center; justify-content: space-between;
    padding: 0 28px 0 29px; font-size: 17.5px; color: var(--text-main);
    border-bottom: 1px solid var(--divider); height: 70px;
  }
  .topic.first { height: 68px; border-bottom: none; }
  .spacer { flex: 1; border-bottom: 1px solid var(--divider); }
  .tab-bar {
    height: 82px; flex: none; display: flex; justify-content: space-around;
    padding: 10px 8px 0;
  }
  .tab {
    width: 96px; display: flex; flex-direction: column; align-items: center; gap: 6px;
    font-size: 16px; color: var(--text-heading);
  }
  .tab svg { stroke: var(--icon); }
  .tab.active { color: var(--brand-red); }
  .tab.active svg { stroke: var(--brand-red); }
</style>
</head>
<body>
<main class="screen">
  <header class="app-header">
    <div class="status-bar">
      <span class="status-time">9:41</span>
      <span class="status-icons">
        <svg width="24" height="16" viewBox="0 0 24 16" fill="#fff"><rect x="0" y="10" width="4" height="6" rx="1"/><rect x="6" y="7" width="4" height="9" rx="1"/><rect x="12" y="4" width="4" height="12" rx="1"/><rect x="18" y="0" width="4" height="16" rx="1"/></svg>
        <svg width="22" height="16" viewBox="0 0 22 16" fill="none" stroke="#fff" stroke-width="2.4" stroke-linecap="round"><path d="M2 5.5a13 13 0 0 1 18 0"/><path d="M5.5 9a8 8 0 0 1 11 0"/><circle cx="11" cy="13" r="1.6" fill="#fff" stroke="none"/></svg>
        <svg width="34" height="16" viewBox="0 0 34 16"><rect x="1" y="1" width="28" height="14" rx="4" fill="none" stroke="#fff" stroke-width="1.6"/><rect x="3.5" y="3.5" width="23" height="9" rx="2" fill="#fff"/><rect x="31" y="5" width="2" height="6" rx="1" fill="#fff"/></svg>
      </span>
    </div>
    <div class="title-bar">
      <svg width="30" height="22" viewBox="0 0 30 22" stroke="#fff" stroke-width="2.6" stroke-linecap="round"><path d="M1 2h28M1 11h28M1 20h20"/></svg>
      <h1>Support</h1>
      <svg width="30" height="32" viewBox="0 0 30 32" fill="none" stroke="#fff" stroke-width="2" stroke-linejoin="round"><path d="M6 23V14a8 8 0 0 1 16 0v9l3 3H3z"/><path d="M11 28a3 3 0 0 0 6 0"/><circle cx="24" cy="6" r="5" fill="var(--online)" stroke="none"/></svg>
    </div>
  </header>

  <div class="search">
    <svg width="24" height="24" viewBox="0 0 24 24" fill="none" stroke="#777" stroke-width="2"><circle cx="10" cy="10" r="8"/><path d="M16 16l6 6" stroke-linecap="round"/></svg>
    <span>Search here...</span>
  </div>

  <div class="section-label">Transactions Related</div>
  <div class="topic first">Issue with the transaction <svg width="12" height="20" viewBox="0 0 12 20" fill="none" stroke="#444" stroke-width="1.8"><path d="M2 2l8 8-8 8"/></svg></div>

  <div class="section-label">Others Topics</div>
  <div class="topic">Call / Email / Chat <svg width="12" height="20" viewBox="0 0 12 20" fill="none" stroke="#444" stroke-width="1.8"><path d="M2 2l8 8-8 8"/></svg></div>
  <div class="topic">Payment Methods <svg width="12" height="20" viewBox="0 0 12 20" fill="none" stroke="#444" stroke-width="1.8"><path d="M2 2l8 8-8 8"/></svg></div>
  <div class="topic">Money Transfers <svg width="12" height="20" viewBox="0 0 12 20" fill="none" stroke="#444" stroke-width="1.8"><path d="M2 2l8 8-8 8"/></svg></div>
  <div class="topic">Recharge &amp; Billpay <svg width="12" height="20" viewBox="0 0 12 20" fill="none" stroke="#444" stroke-width="1.8"><path d="M2 2l8 8-8 8"/></svg></div>
  <div class="topic">Offers / Referral <svg width="12" height="20" viewBox="0 0 12 20" fill="none" stroke="#444" stroke-width="1.8"><path d="M2 2l8 8-8 8"/></svg></div>
  <div class="topic">Website / App payments <svg width="12" height="20" viewBox="0 0 12 20" fill="none" stroke="#444" stroke-width="1.8"><path d="M2 2l8 8-8 8"/></svg></div>
  <div class="topic">Local Stores / Shops <svg width="12" height="20" viewBox="0 0 12 20" fill="none" stroke="#444" stroke-width="1.8"><path d="M2 2l8 8-8 8"/></svg></div>
  <div class="topic">Apps <svg width="12" height="20" viewBox="0 0 12 20" fill="none" stroke="#444" stroke-width="1.8"><path d="M2 2l8 8-8 8"/></svg></div>
  <div class="topic">FAQs <svg width="12" height="20" viewBox="0 0 12 20" fill="none" stroke="#444" stroke-width="1.8"><path d="M2 2l8 8-8 8"/></svg></div>
  <div class="spacer"></div>

  <nav class="tab-bar">
    <div class="tab">
      <svg width="32" height="32" viewBox="0 0 32 32" fill="none" stroke-width="2" stroke-linejoin="round"><path d="M3 15L16 3l13 12"/><path d="M7 12v17h7v-9h4v9h7V12"/></svg>
      Home
    </div>
    <div class="tab">
      <svg width="32" height="32" viewBox="0 0 32 32" fill="none" stroke-width="2" stroke-linejoin="round"><path d="M5 10h22v20H5z"/><path d="M11 13V7a5 5 0 0 1 10 0v6"/></svg>
      Stores
    </div>
    <div class="tab">
      <svg width="32" height="32" viewBox="0 0 32 32" fill="none" stroke-width="2"><circle cx="16" cy="16" r="14"/><circle cx="16" cy="12" r="5"/><path d="M7 26a10 10 0 0 1 18 0"/></svg>
      Account
    </div>
    <div class="tab active">
      <svg width="32" height="32" viewBox="0 0 32 32" fill="none" stroke-width="2.2" stroke-linecap="round"><path d="M5 20v-5a11 11 0 0 1 22 0v5"/><rect x="4" y="17" width="6" height="9" rx="2"/><rect x="22" y="17" width="6" height="9" rx="2"/><path d="M25 26c0 3-3 4-7 4"/></svg>
      Support
    </div>
    <div class="tab">
      <svg width="32" height="32" viewBox="0 0 32 32" fill="none" stroke-width="2" stroke-linecap="round" stroke-linejoin="round"><path d="M4 10h22M21 5l5 5-5 5"/><path d="M28 22H6M11 17l-5 5 5 5"/></svg>
      History
    </div>
  </nav>
</main>
</body>
</html>
```